High End Personalized Functional Medicine in Women's Health

We are adding new and exciting personalized medicine services to our Women's Health Care practice focusing on health optimization and anti-aging as well as hormone replacement therapy and need a high end brochure to educate patients about these services. We would like to see a zen-like design that has feminine appeal. Our office colors are vibrant but soothing. We have utilized the concepts of feng shui to optimize our positive energy. The exterior of the building is peach and cream and these colors would blend with that energy The final design should communicate a sense that you can take control of your health and aging.

Target Market(s)

Females age 35-65 with annual income >$75000/year

Industry/Entity Type

Health And Wellness

Logo Text

Bright Path is the company name. Our sister company is Corva Ridge Ob/Gyn

Font styles to use
Serif

Colors

Designer to choose colors to be used in the design.

Requirements
Must have
• My project must have clean lines. I like a strong feminine appearance, not a fluffy curvy feminine look. Professional appearance, Brochure would be on thicker card stock. A strong front page that makes you want to open the brochure
Nice to have
• Eye catching photos that complement our message . I am not tied to the peach and cream color recommendation, but find those colors feminine but not so cliche as pinks and purples.
Should not have
• frilly design

```html
<!DOCTYPE html>
<html lang="en">
<head>
<meta charset="utf-8">
<title>Bright Path Functional Medicine – Brochure</title>
<link href="https://fonts.googleapis.com/css2?family=Montserrat:wght@400;500;600;700;800&display=swap" rel="stylesheet">
<style>
  :root{
    --stage:#e3e3e6;
    --paper:#ffffff;
    --paper-soft:#f1f1f0;
    --peach:#e2b896;
    --peach-deep:#c98f68;
    --ink:#161616;
    --ink-soft:#4a4a4a;
    --photo-grey-a:#d9d9d9;
    --photo-grey-b:#8e8e8e;
    --photo-warm-a:#e9e3d8;
    --photo-warm-b:#b9c7b0;
  }
  *{box-sizing:border-box;margin:0;padding:0}
  html,body{width:1200px;height:2400px;overflow:hidden}
  body{background:var(--stage);font-family:"Montserrat",Arial,sans-serif;color:var(--ink);position:relative}

  .page{position:absolute;width:540px;height:740px;background:var(--paper);overflow:hidden;box-shadow:0 12px 30px rgba(0,0,0,.12)}
  .spread{position:absolute;left:60px;width:1080px;height:740px;box-shadow:0 12px 30px rgba(0,0,0,.14)}
  .spread .page{box-shadow:none;top:0}
  .spread .page.left{left:0}
  .spread .page.right{left:540px}
  .spread .fold{position:absolute;left:539px;top:0;width:2px;height:740px;background:rgba(0,0,0,.06);z-index:5}

  .photo{position:absolute}
  .photo.mono{background:linear-gradient(135deg,var(--photo-grey-a),var(--photo-grey-b))}
  .photo.warm{background:linear-gradient(135deg,var(--photo-warm-a),var(--photo-warm-b))}
  .photo.framed{border:5px solid var(--paper);box-shadow:0 2px 6px rgba(0,0,0,.15)}

  .accent{color:var(--peach)}

  /* Front cover */
  .cover .cover-photo{left:130px;top:0;right:0;height:560px}
  .cover .side-mark{position:absolute;left:0;top:40px;width:130px;height:470px;display:flex;align-items:center;justify-content:center}
  .cover .side-mark span{writing-mode:vertical-rl;transform:rotate(180deg);font-weight:800;font-size:54px;letter-spacing:1px;white-space:nowrap}
  .cover .cover-band{position:absolute;left:0;right:0;top:520px;height:200px;background:var(--peach);padding:30px 40px 0 40px}
  .cover .band-line{font-weight:800;font-size:25px;letter-spacing:.5px;white-space:nowrap}
  .cover .band-line .light{color:var(--paper)}
  .cover .band-title{font-weight:800;font-size:66px;line-height:1;color:var(--paper);letter-spacing:2px}
  .cover .band-url{font-weight:600;font-size:13px;margin-top:12px;letter-spacing:.5px}

  /* Back page */
  .back{background:var(--paper-soft)}
  .back .back-heading{position:absolute;top:140px;left:0;right:0;text-align:center;font-weight:800;font-size:34px;letter-spacing:1px}
  .back .family-photo{left:105px;top:190px;width:330px;height:230px;z-index:2;border:4px solid var(--paper)}
  .back .back-band{position:absolute;left:0;right:0;top:380px;height:260px;background:var(--peach);padding:60px 40px 0}
  .back .caption{text-align:center;font-weight:800;font-size:15px;letter-spacing:.8px;margin-bottom:8px}
  .back .bio{font-size:10.5px;line-height:1.45;text-align:center;color:var(--ink)}
  .back .contact{display:flex;align-items:center;gap:10px;margin-top:14px;font-size:11.5px;font-weight:700}
  .back .contact .divider{width:1px;height:14px;background:var(--ink)}
  .back .contact svg{width:13px;height:13px;display:block}

  /* Inside left */
  .inside-left .lead{position:absolute;left:50px;top:60px;width:440px;font-weight:800;font-size:16px;line-height:1.3;letter-spacing:.3px;text-transform:uppercase}
  .inside-left .rule{position:absolute;left:50px;top:172px;width:60px;height:2px;background:var(--peach)}
  .inside-left .body{position:absolute;left:50px;top:190px;width:440px;font-size:11px;line-height:1.55;color:var(--ink-soft)}
  .inside-left .body p+p{margin-top:8px}
  .inside-left .care-photo{left:50px;top:400px;width:220px;height:250px}
  .inside-left .small-photo-a{left:285px;top:440px;width:170px;height:100px}
  .inside-left .small-photo-b{left:285px;top:550px;width:170px;height:100px}
  .inside-left .page-mark{position:absolute;left:50px;top:680px;font-weight:800;font-size:18px;letter-spacing:.5px}

  /* Inside right */
  .inside-right .offset-block{position:absolute;left:420px;top:40px;width:90px;height:310px;background:var(--peach)}
  .inside-right .visit-photo{left:55px;top:30px;width:440px;height:300px}
  .inside-right .section{position:absolute;left:55px;width:440px}
  .inside-right .section.why{top:370px}
  .inside-right .section.who{top:505px}
  .inside-right h2{font-weight:800;font-size:14.5px;letter-spacing:.6px;line-height:1.25;text-transform:uppercase}
  .inside-right h2 .accent{display:block}
  .inside-right p{font-size:11px;line-height:1.5;color:var(--ink-soft);margin-top:8px}
  .inside-right .url-bar{position:absolute;left:190px;right:30px;top:685px;height:26px;background:var(--peach);display:flex;align-items:center;justify-content:center;font-weight:700;font-size:12px;letter-spacing:.4px}
</style>
</head>
<body>

  <section class="page cover" style="left:330px;top:40px">
    <div class="photo mono cover-photo" role="img" aria-label="Black and white photo of a smiling female doctor with stethoscope and clipboard, a male colleague behind her"></div>
    <div class="side-mark"><span><span class="accent">BRIGHT</span> PATH</span></div>
    <div class="cover-band">
      <div class="band-line">BRIGHT PATH <span class="light">FUNCTIONAL</span></div>
      <div class="band-title">MEDICINE</div>
      <div class="band-url">www.brightpathfunctionalmedicine.com</div>
    </div>
  </section>

  <section class="spread" style="top:840px">
    <div class="page left back">
      <div class="back-heading"><span class="accent">BRIGHT</span> PATH</div>
      <div class="photo mono family-photo" role="img" aria-label="Black and white family portrait of the doctor with her family seated outdoors"></div>
      <div class="back-band">
        <div class="caption">DR. VARGA WITH FAMILY</div>
        <p class="bio">Dr. Elena Varga specializes in women's health and has over 25 years of experience. She is an expert in bio-identical hormone replacement therapy and has been a certified bio-identical hormone pellet practitioner for over 10 years. Dr. Varga has been practicing functional medicine for many years with a primary focus on hormone therapy, medical weight loss, and lifestyle change.</p>
        <div class="contact">
          <svg viewBox="0 0 24 24" aria-hidden="true"><path fill="#161616" d="M6.6 10.8a15.1 15.1 0 0 0 6.6 6.6l2.2-2.2c.3-.3.7-.4 1-.2 1.1.4 2.3.6 3.6.6.6 0 1 .4 1 1V20c0 .6-.4 1-1 1A17 17 0 0 1 3 4c0-.6.4-1 1-1h3.5c.6 0 1 .4 1 1 0 1.3.2 2.5.6 3.6.1.3 0 .7-.2 1z"/></svg>
          <span>555.014.2290</span>
          <span class="divider"></span>
          <svg viewBox="0 0 24 24" aria-hidden="true"><path fill="#161616" d="M12 3C6.5 3 2 6.6 2 11c0 2.2 1.1 4.2 3 5.7V21l4.1-2.3c.9.2 1.9.3 2.9.3 5.5 0 10-3.6 10-8s-4.5-8-10-8z"/></svg>
          <span>www.brightpathfunctionalmedicine.com</span>
        </div>
      </div>
    </div>
    <div class="page right cover">
      <div class="photo mono cover-photo" role="img" aria-label="Black and white photo of a smiling female doctor with stethoscope and clipboard, a male colleague behind her"></div>
      <div class="side-mark"><span><span class="accent">BRIGHT</span> PATH</span></div>
      <div class="cover-band">
        <div class="band-line">BRIGHT PATH <span class="light">FUNCTIONAL</span></div>
        <div class="band-title">MEDICINE</div>
        <div class="band-url">www.brightpathfunctionalmedicine.com</div>
      </div>
    </div>
    <div class="fold"></div>
  </section>

  <section class="spread" style="top:1620px">
    <div class="page left inside-left">
      <h1 class="lead">Functional medicine's aim is to heal the physical body in order to engage in our life purpose of connection <span class="accent">and emotional and spiritual growth.</span></h1>
      <div class="rule"></div>
      <div class="body">
        <p>Dr. Elena Varga specializes in women's health and has over 25 years of experience. She works closely with each patient to understand the whole person, looking at hormones, nutrition, sleep, stress and daily habits together. Her approach blends careful testing with a clear plan, so every woman leaves with steps she can follow at home. Dr. Halden joins the practice as a partner in functional care, offering added support for weight, energy and healthy aging.</p>
        <p>What do patients say about their experience with Dr. Varga? Patient quote area.</p>
      </div>
      <div class="photo warm care-photo" role="img" aria-label="Photo of a caregiver in blue scrubs walking arm in arm with an elderly woman in a garden"></div>
      <div class="photo warm small-photo-a" role="img" aria-label="Photo of a doctor consulting with a patient at a desk"></div>
      <div class="photo warm small-photo-b" role="img" aria-label="Photo of a doctor speaking with a woman in a clinic"></div>
      <div class="page-mark"><span class="accent">BRIGHT</span> PATH</div>
    </div>
    <div class="page right inside-right">
      <div class="offset-block"></div>
      <div class="photo warm framed visit-photo" role="img" aria-label="Photo of a nurse in teal scrubs holding hands with a smiling senior woman on a yellow sofa"></div>
      <div class="section why">
        <h2>Why should you consider a <span class="accent">functional medicine visit?</span></h2>
        <p>You are tired of feeling tired. You can't even focus on the future because you are so overwhelmed. The pain of being unable to think clearly and being too tired to exercise are your daily reality. Your life goals seem like too much to think about, you just have to get through today.</p>
      </div>
      <div class="section who">
        <h2>Who else should consider a <span class="accent">functional medicine visit?</span></h2>
        <p>You want to achieve OPTIMAL health with a personalized medicine approach. You are eating well, exercising and engaging in stress reducing activities such as meditation. You want to know how to minimize the effects of aging and are ready to take a proactive approach in getting to the highest level of health you can achieve.</p>
      </div>
      <div class="url-bar">www.brightpathfunctionalmedicine.com</div>
    </div>
    <div class="fold"></div>
  </section>

</body>
</html>
```